One of a Kind Clean Business Card

We need to design a new business card template for our company. Our company designs and produced merchandising displays. You can see a sample of what we produce on our site www.qorvatrim.com. I have uploaded our logo in vector format, as well as a picture of our current business cards. We want a totally different look. We want simple and clean, looking forward to seeing what people create.
Updates

I would like to update the address for Teblo Display Group Inc. 418 N Harlow Ln Arlington Heights, IL 60117 Would also note. No QR codes

Industry/Entity Type

Business

Contact Information for Business Card

Need a 1 sided business card designed.

Font styles to use
Serif

Requirements
Must have
• Easy to view; Clean Design
Nice to have
• Features that promote engineering and creativity
Should not have
• Too much clutter, keep it simple

```html
<!DOCTYPE html>
<html lang="en">
<head>
<meta charset="utf-8">
<title>Teblo Display Group Inc. – Business Card</title>
<link rel="stylesheet" href="https://fonts.googleapis.com/css2?family=Open+Sans:wght@400;500&display=swap">
<style>
  :root {
    --backdrop: #8a8a8a;
    --card-light: #f3f3f3;
    --card-dark: #000000;
    --brand-red: #8b1a1f;
    --ink: #2b2b2b;
    --paper-white: #ffffff;
  }
  * { margin: 0; padding: 0; box-sizing: border-box; }
  html, body { width: 1200px; height: 900px; overflow: hidden; }
  body {
    background: var(--backdrop);
    font-family: "Open Sans", Arial, sans-serif;
    position: relative;
  }
  .card {
    position: absolute;
    top: 200px;
    width: 310px;
    height: 502px;
  }
  .card--front {
    left: 265px;
    background: var(--card-light);
    border-radius: 70px 0 70px 0;
  }
  .card--back {
    left: 641px;
    width: 309px;
    background: var(--card-dark);
    border-radius: 0 70px 0 70px;
  }
  .brand-name {
    position: absolute;
    font-weight: 400;
    font-size: 23px;
    line-height: 1.2;
    letter-spacing: 0.2px;
  }
  .card--front .brand-name { left: 27px; top: 86px; color: var(--brand-red); }
  .card--back .brand-name { left: 35px; top: 214px; color: var(--paper-white); }

  .contact { position: absolute; left: 26px; top: 302px; color: var(--ink); }
  .contact__person {
    color: var(--brand-red);
    font-size: 19px;
    font-weight: 400;
    letter-spacing: 0.2px;
    margin-bottom: 14px;
  }
  .contact__address { font-size: 13px; line-height: 18px; margin-bottom: 8px; }
  .contact__list { list-style: none; font-size: 13px; line-height: 18px; }
  .contact__list li { display: flex; align-items: center; gap: 6px; }
  .contact__icon { width: 11px; height: 11px; fill: var(--brand-red); flex: none; }
</style>
</head>
<body>
  <section class="card card--front" aria-label="Business card front">
    <p class="brand-name">Teblo<br>Display Group Inc.</p>
    <div class="contact">
      <h1 class="contact__person">DANA KESSLER</h1>
      <p class="contact__address">275 Orchard Ave.<br>Brenford,IL 60142</p>
      <ul class="contact__list">
        <li>
          <svg class="contact__icon" viewBox="0 0 12 12" aria-hidden="true"><path d="M1 4c0-2 2-3 5-3s5 1 5 3l-2 1-1-2H4L3 5zM3 6h6l1 5H2z"/></svg>
          815-555-0142
        </li>
        <li>
          <svg class="contact__icon" viewBox="0 0 12 12" aria-hidden="true"><path d="M3 0h6v12H3zM4 1.5v8h4v-8z"/></svg>
          312-555-0176
        </li>
        <li>
          <svg class="contact__icon" viewBox="0 0 12 12" aria-hidden="true"><path d="M0 2h12v8H0zM1 3l5 4 5-4v-.2H1z"/></svg>
          dkessler@qorvatrim.com
        </li>
        <li>
          <svg class="contact__icon" viewBox="0 0 12 12" aria-hidden="true"><circle cx="6" cy="6" r="5.5"/><path d="M6 .5v11M.5 6h11" stroke="#f3f3f3" stroke-width="1"/></svg>
          www.qorvatrim.com
        </li>
      </ul>
    </div>
  </section>

  <section class="card card--back" aria-label="Business card back">
    <p class="brand-name">Teblo<br>Display Group Inc.</p>
  </section>
</body>
</html>
```